Building Maintenance Flyer specialising in hot and silent pressure cleaning

Hi. I love this flyer. I would like something similar but with hot water pressure washing and building maintenance

Ferro Lane & Services provides high pressure steam cleaning and water blasting services throughout Brisbane and surrounding areas, covering the Industrial, Commercial, Strata and Residential property owners sectors.

FLS combining the cleaning power of heat with state-of-the-art silent equipment, accredited technicians and a steadfast commitment to the environment. We offer the best Prompt, Professional Service.

Fully Accredited & Certified Technicians
100% Satisfaction Guaranteed
We are a family owned and operated business and love what we do. No job is too big or too small and we take pride in our work.
All of our services are undertaken using industry leading equipment and, providing safe and superior results.

Our business is covered by 20 million full public liability insurance and we operate within strict health & safety guidelines, providing all our clients with complete peace of mind. Project plans and risk assessments can also be provided upon request.

BODY CORPORATES

BUILDING FAÇADE CLEANING

CAR PARKS – underground, single and multi level

DRIVE THRU

FOOD PRODUCTION FACILITIES CLEANING SANITISING

SHOPPING CENTRES

BIRD MANAGEMENT AND DECONTAMINATION

GENERAL MAINTENANCE

CONSTRUCTION CLEAN UPS

SPILL MANAGEMENT

CONCRETE CLEANING AND DEGRASING

CONCRETE SEALING

FACTORY CLEANING & CLEAN UP

ENVIRONMENTAL DECONTAMINATION OF HEAVY VEHICLES AND EQUIPMENT

SITE CLEANS AND RUBBISH REMOVAL

MANUFACTURING PLANTS

Target Market(s)

Facility Managers, Commercial and Industrial Property Owners, Property Managers, Schools, Restaurants,

Industry/Entity Type

Pressure Cleaning

Font styles to use
Sans Serif

Colors
0293ce
00a990
33a6d7
33b8a4

Requirements
Must have
• SILENT HOT WATER PRESSURE CLEANING
Runs up to 120 Degrees Celsius
SANITISING - Bin areas, outdoor areas, cafe's, restaurants, schools, drive thru's
Blue's and Greens to link in with our logo

```html
<!DOCTYPE html>
<html lang="en">
<head>
<meta charset="utf-8">
<title>FLS – Building Maintenance Flyer</title>
<link rel="stylesheet" href="https://fonts.googleapis.com/css2?family=Lato:wght@400;700;900&display=swap">
<style>
  :root {
    --blue: #0293ce;
    --blue-deep: #1c87c9;
    --teal: #00a990;
    --teal-soft: #33b8a4;
    --sky: #33a6d7;
    --ink: #1d1d1f;
    --paper: #f4f5f6;
    --backdrop: #e6ebed;
    --gold: #d9ae3b;
    --gold-light: #f3d77a;
  }
  * { box-sizing: border-box; margin: 0; padding: 0; }
  html, body { width: 1200px; height: 960px; overflow: hidden; }
  body {
    background: var(--backdrop);
    font-family: 'Lato', sans-serif;
    color: var(--ink);
  }
  .flyer {
    position: absolute;
    left: 282px; top: 30px;
    width: 636px; height: 900px;
    background: var(--paper);
    overflow: hidden;
    box-shadow: 0 6px 24px rgba(0,0,0,.12);
  }
  .hero-photo {
    position: absolute; left: 0; top: 0;
    width: 636px; height: 418px;
    background: linear-gradient(115deg, #e4eaee 0%, #cfd8de 45%, #8fa2b0 100%);
  }
  .hero-shapes { position: absolute; left: 0; top: 0; }
  .tagline-bar {
    position: absolute; left: 0; top: 11px;
    width: 252px; height: 32px;
    background: var(--blue);
    color: #fff;
    font-weight: 700; font-size: 16px;
    line-height: 32px; padding-left: 22px;
  }
  .brand-name {
    position: absolute; left: 430px; top: 62px;
    width: 200px; text-align: center;
    font-weight: 900; font-size: 50px; letter-spacing: 1px;
    color: var(--blue);
  }
  .headline {
    position: absolute; right: 16px; top: 190px;
    color: #fff; font-weight: 700; font-size: 20px;
  }
  .intro {
    position: absolute; left: 322px; top: 282px; width: 306px;
    color: #fff; font-size: 15px; line-height: 21.5px; text-align: center;
  }
  .guarantee-seal {
    position: absolute; left: 44px; top: 322px;
    width: 118px; height: 118px; border-radius: 50%;
    background: radial-gradient(circle at 40% 35%, var(--gold-light), var(--gold) 70%);
    box-shadow: 0 0 0 6px #c99a2b inset;
  }
  .features {
    position: absolute; left: 0; top: 462px; width: 636px; height: 104px;
  }
  .feature {
    position: absolute; top: 0; text-align: center;
    font-size: 15px; line-height: 20px; font-weight: 700;
  }
  .feature svg { display: block; margin: 0 auto 8px; }
  .feature--hours { left: 20px; width: 176px; }
  .feature--silent { left: 194px; width: 250px; }
  .feature--accredited { left: 445px; width: 176px; }
  .divider {
    position: absolute; top: 470px; width: 2px; height: 94px; background: var(--teal);
  }
  .solutions-panel { position: absolute; left: 0; top: 584px; }
  .solutions-title {
    position: absolute; left: 22px; top: 594px;
    color: #fff; font-weight: 700; font-size: 30px;
  }
  .solutions-list {
    position: absolute; left: 28px; top: 636px; list-style: none;
  }
  .solutions-list li {
    display: flex; align-items: center; gap: 7px;
    color: #fff; font-size: 15px; height: 23px; white-space: nowrap;
  }
  .solutions-list svg { flex: none; }
  .service-photo {
    position: absolute; left: 340px; top: 572px;
    width: 296px; height: 243px;
    background: linear-gradient(135deg, #d9e2e8 0%, #4f7fb3 55%, #2a4f86 100%);
    clip-path: polygon(69px 0, 100% 0, 100% 100%, 0 100%);
  }
  .contact-label {
    position: absolute; left: 396px; top: 832px; width: 180px;
    text-align: center; color: var(--blue-deep);
    font-weight: 700; font-size: 22px;
  }
</style>
</head>
<body>
  <main class="flyer">
    <div class="hero-photo" role="img" aria-label="Technician in blue overalls taking notes in a clean kitchen"></div>

    <svg class="hero-shapes" width="636" height="446" viewBox="0 0 636 446" aria-hidden="true">
      <polygon points="360,175 636,175 636,418 300,418" fill="var(--teal)" opacity=".88"/>
      <polygon points="395,0 425,0 300,418 270,418" fill="var(--blue)" opacity=".85"/>
      <polygon points="425,0 450,0 400,175 375,175" fill="var(--teal)"/>
      <polygon points="450,0 636,0 636,175 400,175" fill="#f4f5f6"/>
      <polygon points="300,418 636,418 636,446 264,446" fill="var(--blue)"/>
      <g fill="var(--teal-soft)">
        <polygon points="262,11 270,11 256,43 248,43"/>
        <polygon points="274,11 282,11 268,43 260,43"/>
        <polygon points="286,11 294,11 280,43 272,43"/>
        <polygon points="298,11 306,11 292,43 284,43"/>
      </g>
      <defs>
        <symbol id="tick" viewBox="0 0 16 16">
          <circle cx="8" cy="8" r="7" fill="none" stroke="#fff" stroke-width="2"/>
          <path d="M4 8 L7 11 L14 3" fill="none" stroke="#fff" stroke-width="2.4"/>
        </symbol>
      </defs>
    </svg>

    <div class="tagline-bar">FLS – servicing Southeast's</div>
    <div class="brand-name">FLS</div>
    <h1 class="headline">ALL COMMERCIAL PROPERTY</h1>
    <p class="intro">Ferro Lane &amp; Services provides high pressure steam cleaning and water blasting services throughout Brisbane and surrounding areas, covering the industrial, commercial, Strata and residential property owners sectors.</p>

    <div class="guarantee-seal" role="img" aria-label="Satisfaction guarantee seal"></div>

    <section class="features">
      <div class="feature feature--hours">
        <svg width="56" height="56" viewBox="0 0 56 56" aria-hidden="true">
          <path d="M46 16 A22 22 0 1 0 50 32" fill="none" stroke="var(--blue)" stroke-width="3"/>
          <polygon points="42,12 50,14 46,21" fill="var(--blue)"/>
          <text x="28" y="34" text-anchor="middle" font-family="Lato, sans-serif" font-weight="900" font-size="15" fill="var(--blue)">24/7</text>
        </svg>
        We operate 24/7,<br>7 days a week
      </div>
      <div class="feature feature--silent">
        <svg width="56" height="56" viewBox="0 0 56 56" aria-hidden="true">
          <path d="M12 22 H34 L31 52 H15 Z" fill="var(--blue)"/>
          <rect x="10" y="19" width="26" height="5" fill="var(--sky)"/>
          <circle cx="16" cy="10" r="3" fill="var(--blue)"/>
          <circle cx="26" cy="7" r="3" fill="var(--blue)"/>
          <line x1="48" y1="4" x2="40" y2="40" stroke="var(--blue)" stroke-width="3"/>
          <path d="M36 38 L46 40 L46 54 L32 52 Z" fill="var(--blue)"/>
        </svg>
        SILENT HOT WATER<br>pressure cleaning (up to 120°C)
      </div>
      <div class="feature feature--accredited">
        <svg width="56" height="56" viewBox="0 0 56 56" aria-hidden="true">
          <rect x="14" y="4" width="30" height="42" rx="3" fill="var(--blue)"/>
          <path d="M29 10 L37 13 V20 C37 25 33 28 29 30 C25 28 21 25 21 20 V13 Z" fill="#fff"/>
          <path d="M25 19 L28 22 L33 16" fill="none" stroke="var(--blue)" stroke-width="2"/>
          <rect x="19" y="34" width="20" height="2" fill="#fff"/>
          <rect x="19" y="39" width="16" height="2" fill="#fff"/>
          <path d="M10 44 H44 V52 H14 A4 4 0 0 1 10 48 Z" fill="var(--sky)"/>
        </svg>
        Fully Accredited &amp;<br>Certified Technicians
      </div>
    </section>
    <span class="divider" style="left:192px"></span>
    <span class="divider" style="left:441px"></span>

    <svg class="solutions-panel" width="636" height="316" viewBox="0 0 636 316" aria-hidden="true">
      <polygon points="0,0 409,0 316,316 0,316" fill="var(--blue-deep)"/>
    </svg>
    <div class="service-photo" role="img" aria-label="Plumber repairing pipes under a sink with tools"></div>

    <h2 class="solutions-title">Solutions For:</h2>
    <ul class="solutions-list">
      <li><svg width="16" height="16" aria-hidden="true"><use href="#tick"/></svg>Sanitising – Bin Areas, Cafés, Schools</li>
      <li><svg width="16" height="16" aria-hidden="true"><use href="#tick"/></svg>Body Corporates</li>
      <li><svg width="16" height="16" aria-hidden="true"><use href="#tick"/></svg>Building Façade Cleaning</li>
      <li><svg width="16" height="16" aria-hidden="true"><use href="#tick"/></svg>Car Parks &amp; Drive Thrus</li>
      <li><svg width="16" height="16" aria-hidden="true"><use href="#tick"/></svg>Food Production Facilities</li>
      <li><svg width="16" height="16" aria-hidden="true"><use href="#tick"/></svg>Shopping Centres</li>
      <li><svg width="16" height="16" aria-hidden="true"><use href="#tick"/></svg>Bird Management</li>
      <li><svg width="16" height="16" aria-hidden="true"><use href="#tick"/></svg>Concrete Cleaning &amp; Sealing</li>
      <li><svg width="16" height="16" aria-hidden="true"><use href="#tick"/></svg>Factory &amp; Construction Clean Ups</li>
      <li><svg width="16" height="16" aria-hidden="true"><use href="#tick"/></svg>Spill Management</li>
      <li><svg width="16" height="16" aria-hidden="true"><use href="#tick"/></svg>General Maintenance</li>
    </ul>

    <div class="contact-label">Contact Us</div>
  </main>
</body>
</html>
```